Brochure Design Project

Job Type:

1 unified, standard format for 4 marketing templates: doorhanger, factsheet, case study, tri-fold for an energy-services company (helping people and utilities save money)

Task Outline:

Generic templates for 4 marketing pieces that can be used-in other words: latin text fill, lots of pictures that can be replaced or modified, very professional and warm look, deliverable can be modified upon purchase for different programs since we participate in constantly changing programs (universal template is what we’re looking for). The 4 pieces should have a standard look and feel (i.e., same design, different size layout)

Task Description:

The templates will be used to inform/attract clients to our energy efficiency and renewable energy programs. These programs include home improvement measures that cut energy costs and can be funded by government rebate programs. Clients range from residential homeowners, small business owners, and mobile home owners (we will modify pictures, insert text upon delivery for each segment). The template will need to be professional and have the ability to be edited by our staff because we constantly have new programs forming.

Target Market(s)

Utilities, residential, mobile home, small commercial

Industry/Entity Type

Home Improvement

Requirements
Must have
• 1. Locations for the following logos:

PowerMark Ally
HTRW
QVN A+
Utility Logo
Tallwick Group
(See example here: http://www.tallwickgroup.example/index.php?option=com_content&view=article&id=148:northvale-fuel-board-manufactured-mobile-homes&catid=44&Itemid=108)

2. Location for a utility disclaimer box (see box at the bottom of the page in the link above)

3. Location for name of program at the top of the page
Nice to have
• Lots of room for pictures (e.g., see second page of this link:http://www.tallwickgroup.example/index.php?option=com_content&view=article&id=148:northvale-fuel-board-manufactured-mobile-homes&catid=44&Itemid=108 )

see also 2nd page: http://www.tallwickgroup.example/index.php?option=com_content&view=article&id=149:corrin-heat-and-light-manufactured-mobile-home-program&catid=44&Itemid=108

Front / back on 4 templates, color

```html
<!DOCTYPE html>
<html lang="en">
<head>
<meta charset="utf-8">
<title>Energy-Saving Products and Services</title>
<link href="https://fonts.googleapis.com/css2?family=Ubuntu:wght@400;500;700&family=Tinos&display=swap" rel="stylesheet">
<style>
:root{
  --sky-deep:#1576c4;
  --sky-mid:#3d9be0;
  --sky-light:#b9dcf4;
  --tab-blue:#1f86cf;
  --header-blue:#2a8de0;
  --leaf-light:#b3d873;
  --leaf:#8dc63f;
  --leaf-deep:#6aa82a;
  --ink-blue:#0d5f9e;
  --text-white:#ffffff;
  --rule:#8aa9bf;
  --disclaimer:#35601a;
  --photo-frame:#222;
}
*{box-sizing:border-box;margin:0;padding:0}
html,body{width:900px;height:1200px;overflow:hidden;background:#fff}
body{font-family:"Ubuntu",sans-serif;position:relative}
.canvas{position:absolute;inset:0;width:900px;height:1200px;overflow:hidden}
.top-band{position:absolute;left:0;top:0;width:900px;height:110px;background:linear-gradient(90deg,var(--leaf-light),var(--leaf) 55%,var(--leaf-light))}
.program-title{position:absolute;left:88px;top:42px;width:746px;height:57px;border-radius:10px;border:2px solid #fff;background:linear-gradient(180deg,#4aa8ee,var(--header-blue) 55%,#1a74c4);box-shadow:0 3px 6px rgba(0,0,0,.3);color:var(--text-white);font-weight:500;font-size:21px;display:flex;align-items:center;justify-content:center;letter-spacing:.3px}
.sky-column{position:absolute;left:0;top:108px;width:238px;height:655px;background:linear-gradient(180deg,var(--sky-deep),var(--sky-mid) 45%,var(--sky-light));border-right:1px solid var(--rule)}
.sky-column::before{content:"";position:absolute;left:25px;top:0;bottom:0;border-left:1px solid rgba(255,255,255,.35)}
.row{position:absolute;left:0;width:900px;border-bottom:1px solid var(--rule)}
.row-lighting{top:108px;height:219px}
.row-water{top:327px;height:218px}
.row-services{top:545px;height:218px}
.section-tab{position:absolute;left:0;top:8px;width:303px;height:51px;border-radius:0 12px 12px 0;background:linear-gradient(180deg,#3a9ce2,var(--tab-blue));border:1px solid rgba(255,255,255,.6);border-left:none;box-shadow:0 2px 4px rgba(0,0,0,.25);color:#fff;font-weight:700;font-size:17.5px;display:flex;align-items:center;padding-left:41px}
.row-services .section-tab{padding-left:39px}
.item-list{position:absolute;left:41px;top:70px;width:200px;list-style:none;color:#fff;font-size:16px;line-height:27px}
.row-services .item-list{left:38px}
.item-list li::before{content:"• "}
.product{position:absolute;background:linear-gradient(180deg,#fafafa,#e9ecee);border-radius:4px}
.service-photo{position:absolute;top:68px;height:140px;border:2px solid var(--photo-frame);box-shadow:1px 2px 4px rgba(0,0,0,.4)}
.grass{position:absolute;left:0;top:763px;width:900px;height:282px;background:linear-gradient(180deg,#ffffff 0%,#eef6e0 30%,#a9d46a 62%,#5c9a22 100%)}
.contact-box{position:absolute;left:360px;top:778px;width:407px;height:168px;border-radius:14px;border:2px solid #7fbde8;background:rgba(255,255,255,.72);text-align:center;color:var(--ink-blue)}
.contact-lead{margin-top:10px;font-size:19.5px;line-height:25px;color:#1a7fd0}
.contact-lead strong{color:var(--ink-blue)}
.contact-phone{font-size:35px;font-weight:700;margin-top:5px;letter-spacing:.5px}
.contact-meta{font-size:11px;line-height:14px;color:#2a8ad6;margin-top:6px}
.logo-strip{position:absolute;left:70px;top:955px;width:762px;height:70px;background:#fff;display:flex;align-items:center;justify-content:space-around;padding:0 10px}
.partner{display:flex;align-items:center;gap:8px;font-weight:700;font-size:15px;color:var(--ink-blue)}
.partner .badge{width:30px;height:30px;background:var(--tab-blue)}
.partner .dot{width:26px;height:26px;border-radius:50%;background:var(--leaf-deep)}
.partner small{display:block;font-weight:700;font-size:10px}
.footer-band{position:absolute;left:0;top:1045px;width:900px;height:155px;background:var(--leaf)}
.disclaimer{position:absolute;left:77px;top:1058px;width:746px;font-family:"Tinos",serif;font-size:8.4px;line-height:10.2px;color:var(--disclaimer);text-align:justify}
</style>
</head>
<body>
<div class="canvas">
  <div class="top-band"></div>
  <h1 class="program-title">ENERGY - SAVING PRODUCTS AND SERVICES</h1>

  <div class="sky-column" role="img" aria-label="Blue sky with soft clouds"></div>

  <section class="row row-lighting">
    <h2 class="section-tab">Lighting Products</h2>
    <ul class="item-list">
      <li>Interior Hardwire Fixtures</li>
      <li>Exterior Hardwire Fixture</li>
      <li>Compact Fluorescent Lamps</li>
    </ul>
    <div class="product" style="left:364px;top:80px;width:108px;height:98px" role="img" aria-label="Round white ceiling light fixture"></div>
    <div class="product" style="left:516px;top:35px;width:140px;height:148px" role="img" aria-label="Black outdoor wall lantern"></div>
    <div class="product" style="left:700px;top:50px;width:60px;height:118px" role="img" aria-label="Spiral compact fluorescent bulb"></div>
  </section>

  <section class="row row-water">
    <h2 class="section-tab">Water/ Gas Saving Products</h2>
    <ul class="item-list">
      <li>Low-flow Showerheads</li>
      <li>Faucet Aerators</li>
      <li>Pipe-wrap</li>
    </ul>
    <div class="product" style="left:414px;top:46px;width:134px;height:130px" role="img" aria-label="Chrome low-flow showerhead"></div>
    <div class="product" style="left:610px;top:70px;width:134px;height:74px" role="img" aria-label="Chrome faucet aerators"></div>
  </section>

  <section class="row row-services">
    <h2 class="section-tab">Energy Saving Services</h2>
    <ul class="item-list">
      <li>Air Duct Leakage Testing and Sealing</li>
      <li>Central Air Conditioning 5 Point Tune Up</li>
    </ul>
    <div class="service-photo" style="left:247px;width:71px;background:linear-gradient(180deg,#b9b4aa,#6d665b)" role="img" aria-label="Flexible air duct in a wall cavity"></div>
    <div class="service-photo" style="left:328px;width:162px;background:linear-gradient(180deg,#8a7050,#c2b8a8)" role="img" aria-label="Insulated ducts in an attic with testing equipment"></div>
    <div class="service-photo" style="left:500px;width:132px;background:linear-gradient(180deg,#c8c2b5,#5a7aa6 60%,#d9d4c8)" role="img" aria-label="Technician sealing a floor register"></div>
    <div class="service-photo" style="left:640px;width:234px;background:linear-gradient(180deg,#9c9484,#4f6f9e 55%,#b8b0a0)" role="img" aria-label="Technician servicing an outdoor air conditioning unit"></div>
  </section>

  <div class="grass" role="img" aria-label="Green grass against a bright sky"></div>

  <div class="contact-box">
    <p class="contact-lead">Call today for more Energy-Efficient<br>home at <strong>NO COST</strong> to you!</p>
    <p class="contact-phone">888-555-0142</p>
    <p class="contact-meta">Monday- Friday 8 a.m. - 5 p.m.<br>www.tallwickgroup.example<br>California Contractors License # 700418</p>
  </div>

  <div class="logo-strip">
    <div class="partner"><span class="badge"></span>PowerMark Ally</div>
    <div class="partner">HTRW</div>
    <div class="partner"><span class="badge"></span>QVN A+</div>
    <div class="partner"><span>NVFB<small>A Marlow Power utility</small></span></div>
    <div class="partner"><span class="dot"></span>Tallwick Group</div>
  </div>

  <div class="footer-band"></div>
  <p class="disclaimer">A disclaimer is generally any statement intended to specify or delimit the scope of rights and obligations that may be exercised and enforced by parties in a legally recognized relationship. In contrast to other terms for legally operative language, the term disclaimer usually implies situations that involve some level of uncertainty, waiver, or risk.<br>A disclaimer may specify mutually agreed and privately arranged terms and conditions as part of a contract; or may specify warnings or expectations to the general public (or some other class of persons) in order to fulfill a duty of care owed to prevent unreasonable risk of harm or injury. Some disclaimers are intended to limit exposure to damages after a harm or injury has already been suffered. Additionally, some kinds of disclaimers may represent a voluntary waiver of a right or obligation that may be owed to the disclaimant.<br>Disclaimers vary in terms of their uniformity. Some may vary depending on the specific context and parties involved, while other types of disclaimers may strictly adhere to a uniform and established set of formalities that are rarely or never modified, except under official authority. Some of these formal disclaimers are required pursuant to industry regulation, qualification for protection under a safe harbor, and other situations where the exact wording of a particular clause or document may be dispositive in the event of a legal dispute.</p>
</div>
</body>
</html>
```